Hearthstone & Basin Works Sales Flyer

We want a sales flyer that outlines our companies strengths with Kitchen & Bath Remodeling. We would like highlight those aspects while also showcasing our ability to do decks and home additions. We want financing packages to be a big part of the flyer.

Target Market(s)

Residential Customers

Requirements
Must have
• Financing options
Highlight Kitchen & bath remodeling
Less subtle is our decks and home additions
Nice to have
• Keep within our logo colors-we are looking for informative flyers that leave homeowners eager to call us after a meeting

```html
<!DOCTYPE html>
<html lang="en">
<head>
<meta charset="utf-8">
<title>Hearthstone &amp; Basin Works Sales Flyer</title>
<link rel="stylesheet" href="https://fonts.googleapis.com/css2?family=Quicksand:wght@300;400;500;600&family=Montserrat:wght@400;600;700&display=swap">
<style>
  :root {
    --navy: #0f1b33;
    --charcoal: #262b36;
    --orange: #f26522;
    --blue: #1a73c9;
    --ink: #333a48;
    --page: #ffffff;
    --backdrop: #e9e6e1;
  }
  * { box-sizing: border-box; margin: 0; padding: 0; }
  html, body {
    width: 1200px; height: 1200px; overflow: hidden;
    background: var(--backdrop);
  }
  .canvas { position: relative; width: 1200px; height: 1200px; }
  .flyer {
    position: absolute; left: 164px; top: 40px;
    width: 644px; height: 828px;
    background: var(--page);
    transform: scale(1.3527); transform-origin: 0 0;
    box-shadow: 0 2px 6px rgba(0,0,0,.18);
    overflow: hidden;
    font-family: "Montserrat", sans-serif;
  }
  .accent-bar-left {
    position: absolute; left: 0; top: 0; width: 18px; height: 320px;
    background: var(--orange); z-index: 3;
  }
  .header {
    position: absolute; left: 18px; top: 0; width: 626px; height: 108px;
    background: var(--navy);
  }
  .brand {
    position: absolute; left: 0; right: 0; top: 58px;
    display: flex; justify-content: center; align-items: center; gap: 8px;
    font-family: "Quicksand", sans-serif; font-weight: 600;
    font-size: 17px; letter-spacing: .5px; color: var(--orange);
    text-transform: uppercase;
  }
  .brand-mark { width: 10px; height: 10px; background: var(--orange); }
  .header-rule {
    position: absolute; top: 105px; height: 2px; background: var(--orange);
  }
  .header-rule.left { left: 0; width: 187px; }
  .header-rule.right { left: 421px; width: 205px; }
  .hero {
    position: absolute; left: 0; top: 108px; width: 644px; height: 320px;
    background:
      linear-gradient(90deg, rgba(255,255,255,.95) 0%, rgba(255,255,255,.75) 30%, rgba(255,255,255,0) 60%),
      linear-gradient(180deg, #d9c9a8 0%, #efe7da 35%, #f4f1ec 55%, #8a7a68 80%, #c9c3bb 100%);
  }
  .hero-title {
    position: absolute; left: 31px; top: 140px; z-index: 2;
    font-family: "Quicksand", sans-serif; font-weight: 300;
    font-size: 50px; line-height: 55px; color: var(--navy);
    text-transform: uppercase; letter-spacing: .5px;
  }
  .intro { position: absolute; left: 0; right: 0; top: 456px; text-align: center; }
  .intro-heading {
    font-weight: 700; font-size: 14px; color: var(--blue); letter-spacing: .3px;
  }
  .intro-body {
    margin: 6px auto 0; width: 600px;
    font-family: "Quicksand", sans-serif; font-weight: 500;
    font-size: 12.2px; line-height: 15px; color: var(--ink);
  }
  .service {
    position: absolute; top: 549px; width: 287px; height: 135px;
  }
  .service.kitchen { left: 18px; background: linear-gradient(120deg, #2a2c30 0%, #3d3f44 45%, #1d1e21 75%, #8d8f8b 100%); }
  .service.bath { left: 339px; background: linear-gradient(120deg, #b8b4ad 0%, #e6e4e0 40%, #f5f4f2 60%, #9f9a92 100%); }
  .service svg { position: absolute; left: 99px; top: 17px; }
  .service-label {
    position: absolute; left: 0; right: 0; top: 59px; text-align: center;
    font-family: "Quicksand", sans-serif; font-weight: 500; font-size: 14px; color: #fff;
  }
  .closing {
    position: absolute; left: 0; right: 0; top: 706px; text-align: center;
    font-weight: 700; font-size: 11.5px; line-height: 15px; color: var(--navy);
    white-space: nowrap;
  }
  .closing .highlight { color: var(--orange); }
  .closing-rule {
    position: absolute; left: 0; top: 751px; width: 602px; height: 2px; background: var(--orange);
  }
  .accent-bar-right {
    position: absolute; left: 625px; top: 725px; width: 19px; height: 103px; background: var(--blue);
  }
  .footer {
    position: absolute; left: 0; top: 755px; width: 625px; height: 73px;
    background: var(--charcoal);
    display: flex; align-items: center;
    font-family: "Quicksand", sans-serif; color: #fff;
  }
  .contact { position: absolute; display: flex; align-items: center; gap: 9px; }
  .contact.phone { left: 31px; font-size: 17px; }
  .contact.email { left: 206px; font-size: 11.5px; }
  .contact.web { left: 441px; font-size: 11.5px; }
</style>
</head>
<body>
<div class="canvas">
  <article class="flyer">
    <div class="accent-bar-left"></div>
    <header class="header">
      <div class="brand"><span class="brand-mark"></span>Hearthstone &amp; Basin Works</div>
      <div class="header-rule left"></div>
      <div class="header-rule right"></div>
    </header>

    <div class="hero" role="img" aria-label="Photo of a bright modern bathroom with twin basins on a timber vanity and a walk-in shower"></div>
    <h1 class="hero-title">Hearthstone &amp;<br>Basin<br>Works</h1>

    <section class="intro">
      <h2 class="intro-heading">— REMODELING MADE AFFORDABLE —</h2>
      <p class="intro-body">Complete kitchen and bath remodeling from first design to final tile, plus custom decks and home additions built to last. Flexible financing packages with low monthly payments and fast approval let you start sooner.</p>
    </section>

    <div class="service kitchen" role="img" aria-label="Photo of a dark modern kitchen with an island">
      <svg width="88" height="100" viewBox="0 0 88 100"><polygon points="44,0 88,25 88,75 44,100 0,75 0,25" fill="#f26522" fill-opacity=".85"/></svg>
      <span class="service-label">Kitchen</span>
    </div>
    <div class="service bath" role="img" aria-label="Photo of a light bathroom with a freestanding tub and vanity">
      <svg width="88" height="100" viewBox="0 0 88 100"><polygon points="44,0 88,25 88,75 44,100 0,75 0,25" fill="#1a73c9" fill-opacity=".85"/></svg>
      <span class="service-label">Bath</span>
    </div>

    <p class="closing">Ask about 0% financing for 12 months on kitchen, bath, deck and addition projects<br><span class="highlight">Call today for your free in-home estimate.</span></p>
    <div class="closing-rule"></div>
    <div class="accent-bar-right"></div>

    <footer class="footer">
      <div class="contact phone">
        <svg width="17" height="17" viewBox="0 0 24 24"><path fill="#f26522" d="M6.6 10.8a15.1 15.1 0 0 0 6.6 6.6l2.2-2.2c.3-.3.7-.4 1-.2 1.1.4 2.300.6 3.6.6.6 0 1 .4 1 1V20c0 .6-.4 1-1 1A17 17 0 0 1 3 4c0-.6.4-1 1-1h3.5c.6 0 1 .4 1 1 0 1.3.2 2.5.6 3.6.1.3 0 .7-.2 1z"/></svg>
        <span>012-555-0148</span>
      </div>
      <div class="contact email">
        <svg width="18" height="13" viewBox="0 0 18 13"><rect x="1" y="1" width="16" height="11" fill="none" stroke="#f26522" stroke-width="1.5"/><path d="M1 1l8 6 8-6" fill="none" stroke="#f26522" stroke-width="1.5"/></svg>
        <span>hello@hearthstonebasin.com</span>
      </div>
      <div class="contact web">
        <svg width="16" height="16" viewBox="0 0 16 16" fill="none" stroke="#f26522" stroke-width="1.4"><circle cx="8" cy="8" r="7"/><ellipse cx="8" cy="8" rx="3" ry="7"/><path d="M1 8h14"/></svg>
        <span>www.hearthstonebasin.com</span>
      </div>
    </footer>
  </article>
</div>
</body>
</html>
```